Qualified Machining Operator Training Program

We need a flyer to advertise a training program to business. I will attach a rough draft "original file" that we need enhanced to look professional. Details to the program are here https://www.halvornskills.org/credentials/machining-credential-qmo/ We want it to look clean and professional.

Please use the information that is on the "original file" rough draft. I have attached an example pdf, the reason I don't like the example is because it has too many words and looks out of date.

Font styles to use
Serif
Sans Serif

```html
<!DOCTYPE html>
<html lang="en">
<head>
<meta charset="utf-8">
<title>Qualified Machining Operator Program</title>
<link rel="stylesheet" href="https://fonts.googleapis.com/css2?family=Poppins:ital,wght@0,700;1,700;1,800&display=swap">
<style>
  :root {
    --red: #e8352c;
    --red-deep: #d42a2a;
    --orange: #f47a35;
    --amber: #f9a43c;
    --gold: #fbc44c;
    --teal: #1aa6a4;
    --teal-light: #2fc4c0;
    --white: #ffffff;
    --ink: #3a2a22;
    --navy: #1f2d5c;
    --silver: #b9bcc4;
  }
  * { margin: 0; padding: 0; box-sizing: border-box; }
  html, body { width: 928px; height: 1200px; overflow: hidden; background: #fff; }
  body { font-family: "Poppins", Arial, sans-serif; }
  .flyer { position: relative; width: 928px; height: 1200px; overflow: hidden; }
  .training-photo {
    position: absolute; inset: 0;
    background: linear-gradient(160deg, #6e6658 0%, #9a938a 30%, #c7c4c0 55%, #5f7fb6 80%, #3a5fa8 100%);
  }
  .shapes { position: absolute; inset: 0; }
  .badge { position: absolute; top: 33px; width: 116px; height: 60px; border-radius: 50%; }
  .badge-primary { left: 653px; background: var(--navy); border: 4px solid var(--silver); }
  .badge-seal { left: 790px; top: 22px; width: 100px; height: 82px; border-radius: 50%; background: var(--silver); border: 6px solid #8d9099; }
  .pillars { position: absolute; left: 775px; top: 240px; width: 130px; list-style: none; }
  .pillar { position: absolute; left: 0; width: 130px; text-align: center; }
  .pillar-icon {
    display: block; margin: 0 auto; width: 104px; height: 104px; border-radius: 50%;
    background: var(--white); border: 8px solid var(--teal); box-shadow: 0 0 0 3px rgba(47,196,192,.5);
  }
  .pillar-icon svg { width: 100%; height: 100%; }
  .pillar-label {
    display: block; margin-top: 4px; color: var(--white); font-weight: 700; font-style: italic;
    font-size: 22px; line-height: 28px; text-shadow: 1px 2px 2px rgba(0,0,0,.55);
  }
  .brand { position: absolute; left: 37px; top: 828px; display: flex; align-items: center; gap: 12px; }
  .brand-mark { width: 48px; height: 48px; background: var(--teal); }
  .brand-name { color: var(--white); font-weight: 700; font-size: 25px; line-height: 29px; }
  .program-title {
    position: absolute; left: 0; right: 0; top: 960px; text-align: center;
    color: var(--white); font-weight: 800; font-style: italic; font-size: 58px; line-height: 76px;
    text-shadow: 3px 4px 0 var(--ink);
  }
  .contacts { position: absolute; left: 142px; top: 1134px; display: flex; gap: 118px; }
  .contact { display: flex; align-items: center; gap: 10px; color: var(--white); font-weight: 700; font-style: italic; font-size: 22px; }
  .contact svg { width: 32px; height: 32px; }
</style>
</head>
<body>
<main class="flyer">
  <div class="training-photo" role="img" aria-label="Photo of trainees gathered around a table-top mechatronics training rig with motor, pneumatic lines and a blue control box"></div>

  <svg class="shapes" viewBox="0 0 928 1200" aria-hidden="true">
    <polygon points="600,0 928,0 928,230 780,120" fill="var(--amber)"/>
    <polygon points="690,0 928,0 928,140 800,110" fill="var(--red)"/>
    <polygon points="0,570 560,930 928,860 928,1200 0,1200" fill="var(--red)"/>
    <polygon points="0,745 470,1000 928,925 928,1200 0,1200" fill="var(--orange)"/>
    <polygon points="0,840 300,1200 0,1200" fill="var(--amber)"/>
    <polygon points="300,1200 560,930 700,1200" fill="var(--gold)" opacity=".7"/>
    <polygon points="690,875 928,850 928,1000" fill="var(--red-deep)"/>
    <polygon points="0,1040 928,1040 928,1200 0,1200" fill="var(--amber)" opacity=".55"/>
  </svg>

  <div class="badge badge-primary" aria-label="Credential badge"></div>
  <div class="badge badge-seal" aria-label="Credential seal"></div>

  <ul class="pillars">
    <li class="pillar" style="top:0">
      <span class="pillar-icon"><svg viewBox="0 0 100 100"><path d="M24 58 a26 26 0 0 1 52 0 z" fill="var(--teal)"/><rect x="20" y="58" width="60" height="7" rx="3" fill="var(--teal)"/><path d="M32 68 q18 20 36 0" fill="none" stroke="var(--teal)" stroke-width="5"/></svg></span>
      <span class="pillar-label">Safety</span>
    </li>
    <li class="pillar" style="top:157px">
      <span class="pillar-icon"><svg viewBox="0 0 100 100"><circle cx="50" cy="44" r="22" fill="var(--teal)"/><path d="M38 62 l-6 22 l10-5 l6 9 l2-22 z M62 62 l6 22 l-10-5 l-6 9 l-2-22 z" fill="var(--teal)"/><path d="M40 44 l7 7 l13-13" fill="none" stroke="#fff" stroke-width="5"/></svg></span>
      <span class="pillar-label">Quality</span>
    </li>
    <li class="pillar" style="top:315px">
      <span class="pillar-icon"><svg viewBox="0 0 100 100"><circle cx="40" cy="44" r="16" fill="none" stroke="var(--teal)" stroke-width="9" stroke-dasharray="6 4"/><circle cx="66" cy="62" r="11" fill="none" stroke="var(--teal)" stroke-width="7" stroke-dasharray="5 3"/></svg></span>
      <span class="pillar-label">Processes</span>
    </li>
    <li class="pillar" style="top:456px">
      <span class="pillar-icon"><svg viewBox="0 0 100 100"><path d="M30 74 l28-28 a14 14 0 1 1 8 -6 l-28 28 z" fill="var(--teal)"/><circle cx="66" cy="34" r="6" fill="#fff"/></svg></span>
      <span class="pillar-label">Maintenance<br>Awareness</span>
    </li>
  </ul>

  <div class="brand">
    <span class="brand-mark"></span>
    <span class="brand-name">MARLOWE<br>CONSULTING INC</span>
  </div>

  <h1 class="program-title">Qualified Machining<br>Operator Program</h1>

  <div class="contacts">
    <span class="contact"><svg viewBox="0 0 32 32"><circle cx="16" cy="16" r="14" fill="none" stroke="#fff" stroke-width="2.5"/><path d="M11 9 l3 0 l1 4 l-2 2 q2 4 5 5 l2-2 l4 1 l0 3 q-1 2-3 2 q-12-2-12-13 q0-2 2-2z" fill="#fff"/></svg>555 014 2290</span>
    <span class="contact"><svg viewBox="0 0 32 32"><circle cx="16" cy="16" r="14" fill="none" stroke="#fff" stroke-width="2.5"/><rect x="9" y="11" width="14" height="10" fill="#fff"/><path d="M9 11 l7 6 l7-6" fill="none" stroke="var(--orange)" stroke-width="1.5"/></svg>dana@marlowelean.com</span>
  </div>
</main>
</body>
</html>
```